VENTRIX Hardware needs a Flyer Designed

We need a flyer designed for a marketing strategy that is to be launched by VENTRIX. As it is for our hardware division, our logo should go unto the flyer. We are offering to our customers financing on items from $5000 up to $35000. Here are some key words that you may want to include; "building or revovating? you pick the job we've got the financing." The flyer should reflect some sort of home construction and should be very attractive and vibrant. On the flyer it should also state that it's "hassle-free" and; "no down payment", "no collateral", "affordable monthly payments".

Must Haves [en ]: The companies logo. Also it must state the address of the company and contact info which is; 47 Bellweather Lane Penal, Trinidad. Tel: 868-55-VENTRIX. Email must also be listed: info@ventrixholdings.example.

Nice To Haves [en ]: Good quality graphics. something that is captivating and that will hold the attention of our audience.

Should Not Haves [en ]: Should not be too busy.

Industry/Entity Type

Marketing

Requirements
Must have
• The companies logo. Also it must state the address of the company and contact info which is; 47 Bellweather Lane Penal, Trinidad. Tel: 868-55-VENTRIX. Email must also be listed: info@ventrixholdings.example.
Nice to have
• Good quality graphics. something that is captivating and that will hold the attention of our audience.
Should not have
• Should not be too busy.

```html
<!DOCTYPE html>
<html lang="en">
<head>
<meta charset="utf-8">
<title>VENTRIX Hardware – Building or Renovating Flyer</title>
<link rel="stylesheet" href="https://fonts.googleapis.com/css2?family=Roboto+Condensed:wght@700&family=Roboto:ital,wght@0,700;1,400&display=swap">
<style>
  :root {
    --red: #e31e26;
    --navy: #1f2d5c;
    --white: #ffffff;
    --ink: #1a1a1a;
    --stage: #e9e9e9;
    --photo-dark: #4f6378;
    --photo-mid: #9fb4c2;
    --photo-light: #e7eef1;
  }
  * { margin: 0; padding: 0; box-sizing: border-box; }
  html, body { width: 1200px; height: 1000px; overflow: hidden; }
  body { background: var(--stage); position: relative; font-family: "Roboto", Arial, sans-serif; }

  .flyer {
    position: absolute; left: 250px; top: 47px;
    width: 700px; height: 905px;
    background: var(--white); overflow: hidden;
  }
  .hero-art { position: absolute; left: 0; top: 0; width: 700px; height: 612px; }

  .headline {
    position: absolute; left: 21px; top: 34px;
    font-family: "Roboto Condensed", "Arial Narrow", sans-serif; font-weight: 700;
    color: var(--red); font-size: 41px; line-height: 1;
  }
  .subhead {
    position: absolute; left: 23px; top: 94px;
    font-family: "Roboto Condensed", "Arial Narrow", sans-serif; font-weight: 700;
    color: var(--navy); font-size: 33px; line-height: 40px;
  }
  .brand {
    position: absolute; left: 522px; top: 34px;
    display: flex; align-items: center; gap: 8px;
  }
  .brand-mark { width: 22px; height: 22px; background: var(--red); }
  .brand-name {
    font-family: "Roboto Condensed", "Arial Narrow", sans-serif; font-weight: 700;
    color: var(--navy); font-size: 34px; line-height: 1;
  }
  .offer {
    position: absolute; right: 42px; top: 561px;
    font-family: "Roboto Condensed", "Arial Narrow", sans-serif; font-weight: 700;
    color: var(--white); font-size: 35px; line-height: 1;
  }

  .benefits { position: absolute; left: 0; top: 650px; width: 700px; height: 140px; }
  .benefit-rail { position: absolute; left: 50px; top: 4px; width: 566px; height: 4px; background: var(--red); }
  .benefit {
    position: absolute; top: 4px; width: 180px; margin-left: -90px;
    display: flex; flex-direction: column; align-items: center;
  }
  .benefit-stem { width: 3px; height: 14px; background: var(--red); }
  .benefit-icon {
    width: 52px; height: 52px; border-radius: 50%;
    background: var(--red); border: 3px solid #f2c7c9;
    display: flex; align-items: center; justify-content: center;
  }
  .benefit-label {
    margin-top: 16px; text-align: center;
    font-style: italic; font-size: 18px; line-height: 25px; color: var(--ink);
  }

  .contact {
    position: absolute; left: 0; top: 842px; width: 700px;
    display: flex; justify-content: center; gap: 14px; align-items: center;
  }
  .contact-item { display: flex; align-items: center; gap: 8px; font-weight: 700; font-size: 14px; color: var(--ink); }
  .contact-icon {
    width: 26px; height: 26px; border-radius: 50%; background: var(--navy);
    display: flex; align-items: center; justify-content: center;
  }
</style>
</head>
<body>
<main class="flyer">
  <svg class="hero-art" viewBox="0 0 700 612" aria-hidden="false">
    <defs>
      <linearGradient id="photoTone" x1="0" y1="0" x2="1" y2="1">
        <stop offset="0" stop-color="var(--photo-dark)"/>
        <stop offset="0.45" stop-color="var(--photo-mid)"/>
        <stop offset="1" stop-color="var(--photo-light)"/>
      </linearGradient>
    </defs>
    <polygon class="hero-photo" role="img" aria-label="Photo: business handshake over a desk with a small model house, a pen and signed papers" points="0,310 700,125 700,612 0,612" fill="url(#photoTone)"/>
    <polygon class="accent-band" points="0,271 700,92 700,126 0,311" fill="var(--red)"/>
    <polygon class="accent-corner" role="img" aria-label="Red panel with small building icons" points="350,553 700,442 700,553" fill="var(--red)"/>
    <polygon class="offer-band" points="80,612 175,553 700,553 700,612" fill="var(--navy)"/>
  </svg>

  <h1 class="headline">Building or Renovating?</h1>
  <p class="subhead">You Pick the Job,<br>We’ve got the Finances!</p>

  <div class="brand">
    <span class="brand-mark"></span>
    <span class="brand-name">VENTRIX</span>
  </div>

  <p class="offer">Get up to $35,000.00</p>

  <section class="benefits">
    <div class="benefit-rail"></div>
    <div class="benefit" style="left:70px">
      <span class="benefit-stem"></span>
      <span class="benefit-icon">
        <svg width="26" height="26" viewBox="0 0 24 24"><path d="M3 10h4v11H3zM9 21h9l3-8v-3h-7l1-5-2-2-4 6z" fill="#fff"/></svg>
      </span>
      <span class="benefit-label">Hassle-free</span>
    </div>
    <div class="benefit" style="left:237px">
      <span class="benefit-stem"></span>
      <span class="benefit-icon">
        <svg width="26" height="26" viewBox="0 0 24 24"><circle cx="12" cy="9" r="6" fill="#fff"/><text x="12" y="12" font-size="9" font-weight="700" text-anchor="middle" fill="#e31e26" font-family="Arial, sans-serif">$</text><path d="M7 16h10l-5 6z" fill="#1f2d5c"/></svg>
      </span>
      <span class="benefit-label">No down payment</span>
    </div>
    <div class="benefit" style="left:414px">
      <span class="benefit-stem"></span>
      <span class="benefit-icon">
        <svg width="26" height="26" viewBox="0 0 24 24"><rect x="3" y="9" width="14" height="10" fill="#fff"/><rect x="9" y="4" width="12" height="9" fill="#1f2d5c" stroke="#fff" stroke-width="1.5"/><rect x="5" y="12" width="8" height="2" fill="#1f2d5c"/></svg>
      </span>
      <span class="benefit-label">No collateral</span>
    </div>
    <div class="benefit" style="left:593px">
      <span class="benefit-stem"></span>
      <span class="benefit-icon">
        <svg width="26" height="26" viewBox="0 0 24 24"><rect x="3" y="5" width="18" height="16" fill="none" stroke="#fff" stroke-width="2"/><rect x="3" y="5" width="18" height="4" fill="#fff"/><path d="M7 2v5M17 2v5" stroke="#fff" stroke-width="2"/><path d="M8 14l3 3 5-6" fill="none" stroke="#fff" stroke-width="2"/></svg>
      </span>
      <span class="benefit-label">Affordable monthly<br>payments</span>
    </div>
  </section>

  <footer class="contact">
    <span class="contact-item">
      <span class="contact-icon"><svg width="16" height="16" viewBox="0 0 24 24"><path d="M12 3l9 8h-3v9h-5v-6h-2v6H6v-9H3z" fill="#fff"/></svg></span>
      47 Bellweather Lane Penal, Trinidad.
    </span>
    <span class="contact-item">
      <span class="contact-icon"><svg width="16" height="16" viewBox="0 0 24 24"><circle cx="12" cy="12" r="4" fill="none" stroke="#fff" stroke-width="2.4"/><path d="M16 9v5a3 3 0 0 0 5 0v-2a9 9 0 1 0-4 7.5" fill="none" stroke="#fff" stroke-width="2.4"/></svg></span>
      info@ventrixholdings.example.
    </span>
    <span class="contact-item">
      <span class="contact-icon"><svg width="16" height="16" viewBox="0 0 24 24"><path d="M3 9c0-3 4-5 9-5s9 2 9 5l-4 1-1-3H8L7 10zM6 13h12l2 7H4z" fill="#fff"/></svg></span>
      868-55-VENTRIX.
    </span>
  </footer>
</main>
</body>
</html>
```